Stationery for Public Accountant Practice

Name of Practice
Holloway Advisory Pty Ltd
Tel: 0417262938
Postal Address : PO Box 482, Elmsford Park, Vic 3187

Target Market(s)

Small Business Clients

Industry/Entity Type

Accounting

Font styles to use
Serif

Requirements
Must have
• Letterhead, business card, With compliments slip
Nice to have
• Conservative

```html
<!DOCTYPE html>
<html lang="en">
<head>
<meta charset="utf-8">
<title>Holloway Advisory – Business Card</title>
<link href="https://fonts.googleapis.com/css2?family=Mulish:wght@400;700&display=swap" rel="stylesheet">
<style>
  :root {
    --backdrop: #d1d1d1;
    --card: #f0f0f0;
    --ink: #3b3b3b;
    --ink-soft: #444444;
    --gold-deep: #b98f2e;
    --gold: #c9a13f;
    --gold-light: #e2b451;
  }
  * { margin: 0; padding: 0; box-sizing: border-box; }
  html, body {
    width: 1200px;
    height: 1041px;
    overflow: hidden;
    background: var(--backdrop);
    font-family: "Mulish", sans-serif;
    color: var(--ink);
  }
  .card {
    position: absolute;
    left: 282px;
    width: 638px;
    height: 366px;
    background: var(--card);
    box-shadow: 0 1px 2px rgba(0,0,0,0.18);
    overflow: hidden;
  }
  .card--front { top: 107px; }
  .card--back { top: 568px; }

  .brand {
    position: absolute;
    left: 42px;
    top: 66px;
    display: flex;
    align-items: center;
    gap: 12px;
  }
  .brand__mark {
    width: 22px;
    height: 22px;
    background: var(--gold);
  }
  .brand__name {
    font-weight: 700;
    font-size: 27px;
    letter-spacing: 0.2px;
    color: var(--ink);
  }

  .person {
    position: absolute;
    left: 44px;
    top: 191px;
  }
  .person__name {
    font-weight: 700;
    font-size: 20px;
    letter-spacing: 0.3px;
    line-height: 1.2;
  }
  .person__title {
    font-size: 15px;
    line-height: 1.3;
    color: var(--ink-soft);
  }

  .contact {
    position: absolute;
    left: 45px;
    top: 276px;
    list-style: none;
    font-size: 15px;
    line-height: 21px;
    color: var(--ink-soft);
  }
  .contact__item {
    display: flex;
    align-items: center;
    gap: 10px;
  }
  .contact__icon { width: 16px; height: 16px; flex: none; }

  .address {
    position: absolute;
    right: 42px;
    top: 276px;
    text-align: right;
    font-size: 15px;
    line-height: 21px;
    color: var(--ink-soft);
    font-style: normal;
  }

  .bands {
    position: absolute;
    left: 0;
    bottom: 0;
    width: 638px;
    height: 19px;
  }

  .back-name {
    position: absolute;
    left: 0;
    right: 0;
    top: 160px;
    text-align: center;
    font-weight: 700;
    font-size: 38px;
    color: var(--gold);
  }
</style>
</head>
<body>
  <svg width="0" height="0" style="position:absolute">
    <defs>
      <linearGradient id="goldBand" x1="0" y1="0" x2="1" y2="0">
        <stop offset="0" stop-color="#b98f2e"/>
        <stop offset="0.6" stop-color="#e2b451"/>
        <stop offset="1" stop-color="#c9a13f"/>
      </linearGradient>
    </defs>
  </svg>

  <section class="card card--front">
    <div class="brand">
      <span class="brand__mark"></span>
      <span class="brand__name">Holloway Advisory Pty Ltd</span>
    </div>

    <div class="person">
      <p class="person__name">DANIEL HOLLOWAY</p>
      <p class="person__title">FCPA</p>
    </div>

    <ul class="contact">
      <li class="contact__item">
        <svg class="contact__icon" viewBox="0 0 16 16" aria-hidden="true">
          <rect width="16" height="16" rx="2" fill="var(--gold)"/>
          <path d="M5 3.5c.6 0 1.5 2 1.5 2.4 0 .5-.9.8-.9 1.2 0 .8 1.5 2.6 2.4 3 .4.1.8-.8 1.3-.8.4 0 2.3.9 2.3 1.5 0 .8-1 1.7-1.8 1.7C7.2 12.5 3.5 8.8 3.5 5.2c0-.8.8-1.7 1.5-1.7z" fill="#f0f0f0"/>
        </svg>
        <span>0417262938</span>
      </li>
      <li class="contact__item">
        <svg class="contact__icon" viewBox="0 0 16 16" aria-hidden="true">
          <rect width="16" height="16" rx="2" fill="var(--gold)"/>
          <rect x="3" y="4.5" width="10" height="7" fill="none" stroke="#f0f0f0" stroke-width="1.1"/>
          <path d="M3 4.5l5 4 5-4" fill="none" stroke="#f0f0f0" stroke-width="1.1"/>
        </svg>
        <span>daniel@hollowayadvisory.com.au</span>
      </li>
    </ul>

    <address class="address">
      PO Box 482<br>
      Elmsford Park, Vic 3187
    </address>

    <svg class="bands" viewBox="0 0 638 19" aria-hidden="true">
      <polygon points="0,6 356,6 345,19 0,19" fill="var(--ink)"/>
      <polygon points="364,0 638,0 638,19 347,19" fill="url(#goldBand)"/>
    </svg>
  </section>

  <section class="card card--back">
    <p class="back-name">Holloway Advisory</p>
  </section>
</body>
</html>
```